Waste Oil Filter collection & disposal

Basically I need a 1 page website for the business called Brenmoor Waste Solutions.
We are a environmental service provider and we collect and dispose of waste oil filters to protect the environment from hazardous waste oil products.

This is the link to our current website: www.brenmoorwaste.co.nz

we want it to look fresh and better than our current website. we may potentially look at getting a new logo designed and are open to ideas/designs if you have any.

Industry/Entity Type

Business

Logo Text

Brenmoor Waste Solutions

Number of Pages Required

1 page

Requirements
Must have
• same colours as current website.
• description of what service we provide please refer to leaflet attached

```html
<!DOCTYPE html>
<html lang="en">
<head>
<meta charset="utf-8">
<title>Brenmoor Waste Solutions</title>
<link href="https://fonts.googleapis.com/css2?family=Montserrat:wght@200;400;500;600;700&display=swap" rel="stylesheet">
<style>
  :root{
    --green:#78b445;
    --green-dark:#4e6e2e;
    --navy:#141a34;
    --navy-soft:#2c3350;
    --ink:#3b3d4a;
    --grey-bg:#eceef2;
    --white:#ffffff;
  }
  *{margin:0;padding:0;box-sizing:border-box}
  html,body{width:806px;height:1200px;overflow:hidden;background:var(--white)}
  body{font-family:'Montserrat',sans-serif;color:var(--ink);position:relative}
  .abs{position:absolute}
  .center{left:0;width:806px;text-align:center}
  .top-rule{top:0;left:0;width:806px;height:4px;background:var(--green)}
  .hero{top:4px;left:0;width:806px;height:292px;
    background:radial-gradient(ellipse at 58% 30%, #4a5070 0%, #262c48 40%, var(--navy) 80%)}
  .brand{top:40px;left:0;width:806px;display:flex;justify-content:center;align-items:center;gap:10px}
  .brand-dot{width:28px;height:28px;border-radius:50%;background:var(--green)}
  .brand-name{font-weight:600;font-size:16px;color:var(--white)}
  .hero-title{top:130px;font-weight:200;font-size:38px;color:var(--white);letter-spacing:.5px}
  .hero-tag{top:180px;font-weight:700;font-size:15px;color:var(--green);letter-spacing:4.5px}
  .hero-edge{top:266px;left:0}
  .hero-badge{top:248px;left:388px;width:32px;height:36px;border-radius:8px;background:var(--green)}
  .intro-head{top:316px;font-weight:600;font-size:13.5px;line-height:18px;color:var(--ink)}
  .divider{height:3px;width:54px;background:var(--green);left:376px}
  .intro-copy{font-size:8.6px;line-height:14px}
  .kicker{font-weight:700;color:var(--green);letter-spacing:3.2px}
  .process{top:510px;left:0}
  .process-art{top:556px;left:96px;width:240px;height:110px;border-radius:6px;
    background:linear-gradient(90deg,#4f6f30 0%,#5f8838 45%,#e8f2de 100%);opacity:.9}
  .process-title{top:563px;left:374px;font-weight:700;font-size:13px;letter-spacing:3.6px;color:var(--white)}
  .process-copy{top:589px;left:374px;width:320px;font-weight:600;font-size:8.4px;line-height:13.6px;color:var(--navy)}
  .steps{list-style:none;font-weight:600;font-size:8.4px;line-height:14px;color:var(--navy)}
  .steps li::before{content:"•";color:var(--white);margin-right:5px}
  .oil{top:692px;left:0;width:806px;height:164px;
    background:radial-gradient(ellipse at 50% 40%, #262c45 0%, var(--navy) 75%)}
  .oil-title{top:759px;font-size:13px;letter-spacing:3.6px}
  .oil-copy{top:786px;font-weight:600;font-size:8.4px;line-height:13.6px;color:var(--white)}
  .quote{width:170px;text-align:center}
  .quote p{font-weight:600;font-size:10px;line-height:15px;color:var(--ink)}
  .quote cite{display:block;margin-top:5px;font-style:normal;font-weight:600;font-size:7.6px;color:var(--green)}
  .contact{top:996px;left:0;width:806px;height:166px;background:var(--grey-bg)}
  .contact-title{top:1031px;font-size:13px;letter-spacing:3.6px}
  .contact-line{top:1051px;font-size:8.4px}
  .contact-line b{font-weight:600}
  .contact-line a{color:var(--green);font-weight:600;text-decoration:none}
  .price{width:130px;text-align:center}
  .price span{display:block;font-size:8.4px}
  .price strong{display:block;font-weight:700;font-size:14px;margin-top:2px}
  .footer{top:1162px;left:0;width:806px;height:38px;background:var(--green);
    display:flex;justify-content:center;align-items:center;gap:10px}
  .footer i{width:7px;height:7px;border-radius:50%;background:var(--white);display:block}
</style>
</head>
<body>
  <div class="abs top-rule"></div>

  <header>
    <div class="abs hero" role="img" aria-label="Close-up photograph of a used oil filter in dark blue tones"></div>
    <div class="abs brand"><span class="brand-dot"></span><span class="brand-name">Brenmoor Waste Solutions Ltd</span></div>
    <h1 class="abs center hero-title">Brenmoor Waste Solutions</h1>
    <p class="abs center hero-tag">KEEPING NEW ZEALAND GREEN</p>
    <svg class="abs hero-edge" width="806" height="32" viewBox="0 0 806 32"><polygon points="0,28 403,8 806,28 806,32 0,32" fill="#ffffff"/></svg>
    <div class="abs hero-badge" role="img" aria-label="Small green oil filter illustration"></div>
  </header>

  <section>
    <h2 class="abs center intro-head">Brenmoor Waste Solutions Ltd service the Lower North Island and<br>specialise in the collection &amp; disposal of oil &amp; fuel filters</h2>
    <div class="abs divider" style="top:366px"></div>
    <p class="abs center intro-copy" style="top:383px">We are passionate about doing our bit in keeping New Zealand<br>Clean and Green. We offer a cost effective system for the collection and disposal of waste oil filters.</p>
    <p class="abs center intro-copy" style="top:424px">Our processes are environmentally friendly and minimise the contamination of landfills.</p>
    <p class="abs center kicker" style="top:450px;font-size:9.6px">WE KEEP YOUR INDUSTRY COMPLIANT</p>
  </section>

  <section>
    <svg class="abs process" width="806" height="206" viewBox="0 0 806 206"><polygon points="0,0 806,0 806,182 403,206 0,182" fill="#78b445"/></svg>
    <div class="abs process-art" role="img" aria-label="Illustration of an oil filter with an arrow pointing to a recycling symbol"></div>
    <h3 class="abs process-title">THE PROCESS</h3>
    <p class="abs process-copy">Filters are collected and transported back to the processing plant. At the processing plant they are:</p>
    <ul class="abs steps" style="top:623px;left:374px"><li>Drained</li><li>Sorted</li><li>Drained again</li></ul>
    <ul class="abs steps" style="top:623px;left:463px"><li>Crushed into bricks</li><li>Drained a third time</li><li>Stacked ready for Metal Recycling</li></ul>
  </section>

  <section>
    <div class="abs oil" role="img" aria-label="Dark photograph of waste oil"></div>
    <svg class="abs" style="top:692px;left:0" width="806" height="24" viewBox="0 0 806 24"><polygon points="0,0 806,0 403,24" fill="#78b445"/></svg>
    <h3 class="abs center kicker oil-title">WHAT HAPPENS TO THE OIL?</h3>
    <p class="abs center oil-copy">All residual oil is collected into our tank and then recycled.<br>Currently we are processing over 2,000 litres of oil a month.</p>
  </section>

  <section>
    <blockquote class="abs quote" style="top:898px;left:113px"><p>“each used oil filter has on average, more than quarter of a litre of used motor oil”</p><cite>- GreenCycle West</cite></blockquote>
    <blockquote class="abs quote" style="top:898px;left:318px"><p>“recycling engine oil protects the environment and conserves energy resources”</p><cite>- Lube Renew Trust</cite></blockquote>
    <blockquote class="abs quote" style="top:898px;left:525px"><p>“one litre of used oil can contaminate one million litres of water”</p><cite>- Harbourview District Council</cite></blockquote>
  </section>

  <section>
    <div class="abs contact"></div>
    <h3 class="abs center kicker contact-title">READY TO HELP YOU</h3>
    <p class="abs center contact-line">Call us on <b>06 555 0142</b> or email <a>info@brenmoorwaste.co.nz</a></p>
    <div class="abs divider" style="top:1080px"></div>
    <div class="abs price" style="top:1100px;left:209px"><span>Monthly Bin Collection:</span><strong>$65.00</strong></div>
    <div class="abs price" style="top:1100px;left:338px"><span>Additional Bins:</span><strong>$35.00</strong></div>
    <div class="abs price" style="top:1100px;left:466px"><span>Account Set Up Fee:</span><strong>$85.00</strong></div>
  </section>

  <footer class="abs footer"><i></i><i></i><i></i></footer>
</body>
</html>
```